I'm a magician . hypnotist also a good barber. I need this all to be shown in good detail on the cards.

Industry/Entity Type

Magician

Contact Information for Business Card

Magician/ hypnotist/barber Rowan Pitt. One of the best. Tel 07421 736204
Email.Trickshears48@fernmail.example
Title of card spell chap.

```html
<!DOCTYPE html>
<html lang="en">
<head>
<meta charset="utf-8">
<title>Spell Chap – Business Card</title>
<link rel="stylesheet" href="https://fonts.googleapis.com/css2?family=Poiret+One&family=Noticia+Text:ital@1&family=Montserrat:wght@400&display=swap">
<style>
  :root {
    --backdrop: #10021f;
    --card-top: #141414;
    --card-mid: #6f6f6f;
    --card-bottom: #d6d6d6;
    --card-edge: #7a7a7a;
    --title-stroke: #f2f2f2;
    --title-fill: #2a2a2a;
    --text-light: #ffffff;
    --text-dark: #3a3a3a;
    --icon: #f4f4f4;
  }
  html, body {
    margin: 0;
    padding: 0;
    width: 1200px;
    height: 900px;
    overflow: hidden;
    background: var(--backdrop);
  }
  .canvas {
    position: relative;
    width: 1200px;
    height: 900px;
  }
  .card {
    position: absolute;
    left: 62px;
    top: 139px;
    width: 1066px;
    height: 588px;
    border: 5px solid var(--card-edge);
    background: linear-gradient(180deg, var(--card-top) 0%, #3a3a3a 25%, var(--card-mid) 50%, #b8b8b8 78%, var(--card-bottom) 100%);
  }
  .card-title {
    position: absolute;
    top: 50px;
    left: 0;
    right: 0;
    margin: 0;
    text-align: center;
    font-family: "Poiret One", sans-serif;
    font-weight: 400;
    font-size: 112px;
    line-height: 1;
    color: var(--title-fill);
    -webkit-text-stroke: 3px var(--title-stroke);
    letter-spacing: 2px;
  }
  .tagline {
    position: absolute;
    top: 240px;
    left: 0;
    right: 0;
    margin: 0;
    text-align: center;
    font-family: "Noticia Text", serif;
    font-style: italic;
    font-size: 34px;
    line-height: 47px;
    color: var(--text-dark);
  }
  .tagline .roles { color: var(--text-light); }
  .contact {
    position: absolute;
    top: 512px;
    display: flex;
    align-items: center;
    gap: 10px;
  }
  .contact-email { left: 58px; }
  .contact-phone { right: 56px; }
  .contact-email .contact-text {
    font-family: "Noticia Text", serif;
    font-style: italic;
    font-size: 26px;
    color: var(--text-dark);
  }
  .contact-phone .contact-text {
    font-family: "Montserrat", sans-serif;
    font-size: 28px;
    color: var(--text-dark);
  }
  .page-curl {
    position: absolute;
    left: 0;
    top: 0;
  }
</style>
</head>
<body>
<div class="canvas">
  <div class="card">
    <h1 class="card-title">Spell Chap</h1>
    <p class="tagline"><span class="roles">Magician/ hypnotist/</span>barber Rowan Pitt. One<br>of the best.</p>

    <div class="contact contact-email">
      <svg class="icon-mail" width="52" height="34" viewBox="0 0 52 34" aria-hidden="true">
        <rect x="1.5" y="1.5" width="49" height="31" fill="none" stroke="var(--icon)" stroke-width="2"/>
        <polyline points="1.5,1.5 26,20 50.5,1.5" fill="none" stroke="var(--icon)" stroke-width="2"/>
        <polyline points="1.5,32.5 20,15" fill="none" stroke="var(--icon)" stroke-width="2"/>
        <polyline points="50.5,32.5 32,15" fill="none" stroke="var(--icon)" stroke-width="2"/>
      </svg>
      <span class="contact-text">Trickshears48@fernmail.example</span>
    </div>

    <div class="contact contact-phone">
      <svg class="icon-phone" width="26" height="44" viewBox="0 0 26 44" aria-hidden="true">
        <rect x="1.5" y="1.5" width="23" height="41" rx="4" fill="none" stroke="var(--icon)" stroke-width="2.5"/>
        <rect x="5" y="6" width="16" height="15" fill="var(--icon)"/>
        <g fill="var(--icon)">
          <rect x="5" y="25" width="4" height="3"/><rect x="11" y="25" width="4" height="3"/><rect x="17" y="25" width="4" height="3"/>
          <rect x="5" y="30" width="4" height="3"/><rect x="11" y="30" width="4" height="3"/><rect x="17" y="30" width="4" height="3"/>
          <rect x="5" y="35" width="4" height="3"/><rect x="11" y="35" width="4" height="3"/><rect x="17" y="35" width="4" height="3"/>
        </g>
      </svg>
      <span class="contact-text">07421 736204</span>
    </div>
  </div>

  <svg class="page-curl" width="1200" height="900" viewBox="0 0 1200 900" aria-hidden="true">
    <defs>
      <linearGradient id="curlShade" x1="0" y1="1" x2="1" y2="0">
        <stop offset="0" stop-color="#1b1b1b"/>
        <stop offset="0.6" stop-color="#3a3a3a"/>
        <stop offset="1" stop-color="#0c0c0c"/>
      </linearGradient>
    </defs>
    <polygon points="1060,740 1140,740 1140,630" fill="var(--backdrop)"/>
    <polygon points="980,780 1140,640 1200,610 1200,630 1100,720" fill="#050008" opacity="0.7"/>
    <polygon points="1060,740 1140,630 1118,712" fill="url(#curlShade)"/>
  </svg>
</div>
</body>
</html>
```